Edgy Fun BBQ sauce label Needed

We are looking for a new label design as we are going to start to sell our competition bbq sauce. We have had multiple 1st place wins using this sauce in NPGA BBQ competitions

The Sauce name is Drizzle Away! The sauce will be bottled in mason jars, I would like the label to play off bbq themes and "sweet heat"

The sauce will be bottled in standard mason jar 16 oz and the label size is (2.3125in” x 9.4375in ) the front logo needs to fit with in (2.3125 tall x 5in across) Since the back will have to have the food label info.

We are looking for a new label design as we are going to start to sell our competition bbq sauce. We have had multiple 1st place wins using this sauce in NPGA BBQ competitions so I would like to have award winning ribbon somewhere on the label.

We have a logo for our BBQ team this can be incorporated but it is not required. If it is incorporated to the design. it does not have to be the focal point.

We are looking for this label to stand out and grab their attention we like to have fun and push the envelope a bit so don't be timid with the design.

Sauce Description: The award winning Dust Off! BBQ team has been bringing our local flavor to the BBQ competition circuit and now we are bringing it straight to your kitchen. Slather Sweat heat on any meat.

Here are some examples of sauces that are popular in competition bbq.

http://hickoryvaultgrill.example/

https://www.tallcedargrills.example/store/bbq-sauce/amber-goat-classic-barbecue-sauce

https://www.tallcedargrills.example/store/bbq-sauce/fieldhands-tangy-250
Updates

I would like to see on the label  in a the sauce name "Drizzle Away!"  then in smaller front "Barbecue Sauce"  - Then optional in yet smaller front "A Sweet Heat Treat" or " A Sweet Heat Treat for any Meat"

With all this I understand the Dust Off logo may not fit which is ok and it does not need to be on the label.

Reason: I know a bunch of Designers had just started to work on this project so I extended the deadline..

Target Market(s)

We are going to focus on catering, farmers markets, fairs, and BBQ competitions

Industry/Entity Type

Store

Font styles to use
Other font styles liked:
• Desdemona

Colors
eb1f27
f37022
fcf9ce
fbed23
faa54b

Requirements
Must have
• The Sauce name - Drizzle Away!
smaller then name but I would like " BBQ Sauce - Treat your meat to a sweet heat"

award winning ribbon or trophy
Nice to have
• A edgy cartoon pig or cow standing over a vantor style kettle grill using a mop style brush slathering sauce on to a rack of bbq ribs

Dust Off! BBQ in matching front from our logo

```html
<!DOCTYPE html>
<html lang="en">
<head>
<meta charset="utf-8">
<title>Drizzle Away! Barbeque Sauce Label</title>
<link rel="stylesheet" href="https://fonts.googleapis.com/css2?family=Federo&family=Oswald:wght@400;500;600&display=swap">
<style>
  :root {
    --sauce-red: #d8202a;
    --sauce-red-deep: #b5161f;
    --sauce-red-light: #ec2a31;
    --gold-border: #fbbf52;
    --banner-gold: #fcc157;
    --title-cream: #fcf9ce;
    --tag-yellow: #fbed23;
    --ink: #241611;
    --cream: #fcf9ce;
    --flag-pink: #f07a78;
    --page: #ffffff;
  }
  html, body {
    margin: 0;
    padding: 0;
    width: 1200px;
    height: 1000px;
    overflow: hidden;
    background: var(--page);
  }
  .label-canvas {
    display: block;
    width: 1200px;
    height: 1000px;
  }
  .tagline {
    font-family: "Oswald", sans-serif;
    font-weight: 500;
    font-size: 21px;
    fill: var(--tag-yellow);
    letter-spacing: 0.3px;
  }
  .sauce-name {
    font-family: "Federo", serif;
    fill: var(--title-cream);
  }
  .sauce-type {
    font-family: "Oswald", sans-serif;
    font-weight: 600;
    font-size: 40px;
    fill: var(--ink);
    letter-spacing: 0.5px;
  }
  .net-weight {
    font-family: "Oswald", sans-serif;
    font-weight: 500;
    font-size: 16px;
    fill: var(--cream);
  }
</style>
</head>
<body>
<svg class="label-canvas" viewBox="0 0 1200 1000" xmlns="http://www.w3.org/2000/svg">
  <defs>
    <radialGradient id="diamond-glow" cx="50%" cy="45%" r="60%">
      <stop offset="0%" stop-color="var(--sauce-red-light)"/>
      <stop offset="70%" stop-color="var(--sauce-red)"/>
      <stop offset="100%" stop-color="var(--sauce-red-deep)"/>
    </radialGradient>
    <filter id="label-shadow" x="-20%" y="-20%" width="140%" height="140%">
      <feDropShadow dx="0" dy="4" stdDeviation="10" flood-color="#000" flood-opacity="0.25"/>
    </filter>
  </defs>

  <g class="label" filter="url(#label-shadow)">
    <polygon class="label-diamond" points="600,150 950,500 600,850 250,500"
             fill="url(#diamond-glow)" stroke="var(--gold-border)" stroke-width="9" stroke-linejoin="miter"/>
  </g>

  <rect class="pig-silhouette" role="img" aria-label="White pig silhouette illustration"
        x="520" y="262" width="160" height="82" rx="30" fill="#ffffff"/>

  <g class="tagline-row">
    <polygon class="tagline-flag" points="414,373 432,373 428,380 432,387 414,387" fill="var(--flag-pink)"/>
    <polygon class="tagline-flag" points="786,373 768,373 772,380 768,387 786,387" fill="var(--flag-pink)"/>
    <text class="tagline" x="600" y="388" text-anchor="middle">TREAT YOUR MEAT TO A SWEET HEAT</text>
    <line class="tagline-rule" x1="430" y1="402" x2="770" y2="402" stroke="var(--gold-border)" stroke-width="1.5"/>
  </g>

  <g class="sauce-name-block">
    <text class="sauce-name" x="600" y="486" text-anchor="middle" font-size="92" textLength="330" lengthAdjust="spacingAndGlyphs">DRIZZLE</text>
    <text class="sauce-name" x="600" y="618" text-anchor="middle" font-size="128" textLength="340" lengthAdjust="spacingAndGlyphs">AWAY!</text>
  </g>

  <g class="sauce-type-banner">
    <path d="M366,640 Q600,662 834,640 Q846,639 845,651 L836,738 Q835,748 824,749 Q600,768 376,749 Q365,748 364,738 L355,651 Q354,639 366,640 Z"
          fill="var(--banner-gold)" stroke="var(--ink)" stroke-width="3"/>
    <text class="sauce-type" x="600" y="718" text-anchor="middle">BARBEQUE SAUCE</text>
  </g>

  <text class="net-weight" x="600" y="797" text-anchor="middle">16 oz</text>
</svg>
</body>
</html>
```